Sympathy Gift Supplier needs packaging designs

We provide sympathy/bereavement gifts such as memorial candles and picture frames for those who recently lost a loved one. We need packaging design for our boxes that will be uplifting and positive, yet elegant.

We have attached our logo in white and black as well as a saying we would like on the box, and what we need on the back panel.
Ignore the black as it was something we were working on for another product.

These products will be given as gifts to people who lost a loved one as remembrance.

• Back panel details (provided)
Memorial quote (provided)
Must be appropriate for this type of product

```html
<!DOCTYPE html>
<html lang="en">
<head>
<meta charset="utf-8">
<title>Serene Grove – Memorial Candle Box</title>
<link rel="stylesheet" href="https://fonts.googleapis.com/css2?family=Amatic+SC:wght@700&family=Great+Vibes&family=Montserrat:wght@400;600;700&display=swap">
<style>
  :root {
    --backdrop: #e4e4e6;
    --violet-deep: #6a3b93;
    --violet-panel-a: #9676ae;
    --violet-panel-b: #ad90c4;
    --lavender-wash: #ddd1e8;
    --lavender-soft: #efe9f4;
    --ink: #1f1f1f;
    --paper: #ffffff;
    --leaf: #7cc242;
  }
  * { box-sizing: border-box; margin: 0; padding: 0; }
  html, body { width: 1200px; height: 1056px; overflow: hidden; }
  body {
    background: linear-gradient(180deg, #efeff0 0%, var(--backdrop) 100%);
    font-family: "Montserrat", sans-serif;
    position: relative;
  }
  .dieline { position: absolute; left: 35px; top: 110px; width: 1130px; height: 803px; }
  .panel {
    position: absolute;
    top: 235px;
    height: 568px;
    overflow: hidden;
    box-shadow: 0 1px 3px rgba(0,0,0,.12);
  }
  .lid {
    position: absolute;
    top: 0;
    height: 235px;
    background: var(--paper);
    display: flex;
    align-items: center;
    justify-content: center;
    box-shadow: 0 1px 3px rgba(0,0,0,.12);
  }
  .side {
    width: 235px;
    background: linear-gradient(160deg, var(--violet-panel-b) 0%, var(--violet-panel-a) 100%);
    display: flex;
    align-items: center;
    justify-content: center;
  }
  .side-frame {
    position: absolute;
    inset: 14px;
    border: 1.5px solid rgba(255,255,255,.9);
  }
  .brand {
    font-family: "Montserrat", sans-serif;
    font-weight: 600;
    display: flex;
    align-items: center;
    gap: 8px;
    white-space: nowrap;
  }
  .brand-dot { border-radius: 50%; flex: none; }
  .brand--light { color: var(--paper); font-size: 19px; }
  .brand--light .brand-dot { width: 14px; height: 14px; border: 1.5px solid var(--paper); }
  .brand--violet { color: var(--violet-deep); font-size: 22px; }
  .brand--violet .brand-dot { width: 16px; height: 16px; background: var(--leaf); }
  .face { width: 330px; background: var(--paper); }
  .wash { position: absolute; left: 0; right: 0; }
  .wash--top { top: 0; height: 100px; background: linear-gradient(180deg, var(--lavender-wash) 0%, var(--lavender-soft) 60%, rgba(255,255,255,0) 100%); }
  .wash--bottom { bottom: 0; height: 170px; background: linear-gradient(0deg, var(--lavender-wash) 0%, var(--lavender-soft) 55%, rgba(255,255,255,0) 100%); }
  .face-brand { position: absolute; left: 0; right: 0; display: flex; justify-content: center; }
  .quote {
    position: absolute; left: 0; right: 0; top: 238px;
    text-align: center;
    font-family: "Amatic SC", sans-serif;
    font-weight: 700;
    font-size: 38px;
    line-height: 41px;
    color: var(--ink);
  }
  .quote-close {
    position: absolute; left: 0; right: 0; top: 402px;
    text-align: center;
    font-family: "Great Vibes", cursive;
    font-size: 58px;
    line-height: 60px;
    color: var(--violet-deep);
  }
  .heart { position: absolute; left: 138px; top: 470px; }
  .about { position: absolute; left: 30px; right: 30px; top: 212px; text-align: center; font-size: 7.6px; line-height: 11px; color: var(--ink); }
  .about strong { font-weight: 700; }
  .instructions { position: absolute; left: 26px; right: 26px; top: 278px; text-align: center; font-size: 7.6px; line-height: 10.5px; color: var(--ink); }
  .instructions h3 { font-size: 8px; font-weight: 700; }
  .warning {
    position: absolute; left: 62px; right: 62px; top: 364px;
    border: 1px solid var(--ink); border-radius: 3px;
    padding: 8px 6px 5px; text-align: center;
    font-size: 7.4px; line-height: 10px; color: var(--ink);
  }
  .warning h3 {
    position: absolute; top: -6px; left: 50%; transform: translateX(-50%);
    background: var(--paper); padding: 0 5px; font-size: 7.6px; font-weight: 700;
  }
  .site { position: absolute; left: 0; right: 0; top: 448px; text-align: center; font-size: 13px; color: var(--ink); }
  .origin { position: absolute; left: 0; right: 0; top: 522px; text-align: center; font-size: 7.6px; font-weight: 700; color: var(--ink); }
</style>
</head>
<body>
  <main class="dieline">
    <div class="lid" style="left:235px; width:330px;">
      <div class="brand brand--violet"><span class="brand-dot"></span>Serene Grove</div>
    </div>
    <div class="lid" style="left:800px; width:330px;">
      <div class="brand brand--violet"><span class="brand-dot"></span>Serene Grove</div>
    </div>

    <section class="panel side" style="left:0;">
      <div class="side-frame"></div>
      <div class="brand brand--light"><span class="brand-dot"></span>Serene Grove</div>
    </section>

    <section class="panel face" style="left:235px;">
      <div class="wash wash--top" role="img" aria-label="Soft lavender watercolour wash"></div>
      <div class="wash wash--bottom" role="img" aria-label="Soft lavender watercolour wash"></div>
      <div class="face-brand" style="top:118px;">
        <div class="brand brand--violet"><span class="brand-dot"></span>Serene Grove</div>
      </div>
      <p class="quote">When the people we love<br>are taken from us,<br>the way to have them live on<br>is to never stop</p>
      <p class="quote-close">Loving Them</p>
      <svg class="heart" width="54" height="54" viewBox="0 0 54 54" aria-hidden="true">
        <path d="M27 50 C18 40 4 30 4 17 C4 9 10 4 16 4 C21 4 25 8 27 12 C29 8 33 4 38 4 C44 4 50 9 50 17 C50 30 36 40 27 50 Z" fill="none" stroke="#a98bc4" stroke-width="2.2"/>
      </svg>
    </section>

    <section class="panel side" style="left:565px;">
      <div class="side-frame"></div>
      <div class="brand brand--light"><span class="brand-dot"></span>Serene Grove</div>
    </section>

    <section class="panel face" style="left:800px;">
      <div class="wash wash--top" role="img" aria-label="Soft lavender watercolour wash"></div>
      <div class="wash wash--bottom" role="img" aria-label="Soft lavender watercolour wash"></div>
      <div class="face-brand" style="top:130px;">
        <div class="brand brand--violet"><span class="brand-dot"></span>Serene Grove</div>
      </div>
      <p class="about"><strong>Serene Grove</strong> is a family owned company and all of our products are carefully designed and crafted with your family in mind.</p>
      <div class="instructions">
        <h3>Burning Instructions:</h3>
        <p>Trim wick to 1/4" before lighting. Keep candle free of any foreign materials including matches and wick trimmings. Only burn the candle on a level, fire resistant surface. Do not burn candle for more than four hours at a time. Stop use when only 1/4" of wax remains.</p>
      </div>
      <div class="warning">
        <h3>WARNING</h3>
        <p>Burn within sight. Keep away from flammable objects.<br>Keep away from children and pets.</p>
      </div>
      <p class="site">www.SereneGrove.com</p>
      <p class="origin">MADE IN CHINA</p>
    </section>
  </main>
</body>
</html>
```